LETTERHEAD & ENVELOPE: eye-catching stationary design for our custom office furniture business

Our company recently rebranded and we are in need of new stationary. Specifically, we need branded letterhead for standard paper size (8.5” x 11”), and matching envelopes, size: #9.

All designs should incorporate our brand colors, brand typeface, and logo. Please view attached brand guidelines document for brand colors, and brand description.

Letterhead: 8.5” x 11” Must include CedarlineKTV Logo, Talbot Greaves Certified Dealer Logo, mailing address, phone number, website, and email address.

Envelope: 9.5” x 4.125” Must include CedarlineKTV Logo, mailing address, and Talbot Greaves Certified Dealer Logo.

Attached files include:

```html
<!DOCTYPE html>
<html lang="en">
<head>
<meta charset="utf-8">
<title>CedarlineKTV Stationery</title>
<link href="https://fonts.googleapis.com/css2?family=Raleway:wght@300;400;700&display=swap" rel="stylesheet">
<style>
:root{
  --backdrop:#c9c9c9;
  --paper:#ececec;
  --sage:#66857a;
  --charcoal:#2a2a2a;
  --ink:#3a3a3a;
  --badge-grey:#6e6e6e;
  --hairline:#dadada;
}
*{margin:0;padding:0;box-sizing:border-box}
html,body{width:1200px;height:1167px;overflow:hidden;background:var(--backdrop);font-family:'Raleway',sans-serif;color:var(--ink)}
.canvas{position:relative;width:1200px;height:1167px}
.sheet{position:absolute;background:var(--paper);overflow:hidden;transform-origin:0 0;box-shadow:0 2px 6px rgba(0,0,0,.12)}
.letterhead{left:30px;top:145px;width:1128px;height:1595px;transform:scale(.55)}
.envelope{left:680px;top:461px;width:1183px;height:590px;transform:scale(.414)}
.art{position:absolute;left:0;top:0}
.abs{position:absolute;white-space:nowrap}
.brand-name{font-weight:300;color:var(--sage);line-height:1;white-space:nowrap}
.letter-header{position:absolute;left:187px;top:100px;width:857px;height:64px;display:flex;align-items:center}
.letter-header .brand-name{font-size:60px;flex:none}
.header-rule{flex:1;height:10px;border-radius:4px;background:var(--sage);margin-left:38px}
.envelope .brand-name{left:154px;top:78px;font-size:58px}
.recipient{left:90px;top:262px;font-size:20px;line-height:28px}
.recipient b{font-weight:700;color:var(--charcoal)}
.recipient b span{color:var(--sage)}
.recipient .tag{color:var(--sage)}
.date{right:84px;top:374px;font-size:19px;color:var(--charcoal)}
.letter-body{position:absolute;left:88px;top:536px;width:954px;font-size:19px;line-height:28px;text-align:justify;color:var(--ink)}
.letter-body p{margin-bottom:28px}
.signature{left:87px;top:1212px;font-size:20px;line-height:29px}
.signature b{font-weight:700;color:var(--charcoal)}
.contacts{position:absolute;font-size:17px;color:var(--charcoal)}
.contacts li{list-style:none;display:flex;align-items:center;gap:9px;height:22px;white-space:nowrap}
.contacts svg{width:16px;height:16px;flex:none}
.letterhead .contacts{left:88px;top:1398px}
.envelope .contacts{left:64px;top:443px;font-size:16px}
.envelope .contacts li{height:27px}
.dealer{font-size:18px;font-weight:400}
.letterhead .dealer{left:630px;top:1466px;color:var(--badge-grey)}
.envelope .dealer{left:592px;top:514px;color:#fff;font-size:16px}
</style>
</head>
<body>
<svg width="0" height="0" style="position:absolute">
  <symbol id="icon-pin" viewBox="0 0 16 16"><rect x=".5" y=".5" width="15" height="15" fill="none" stroke="#66857a"/><path d="M8 3.5a3 3 0 0 1 3 3c0 2.2-3 5.5-3 5.5S5 8.7 5 6.5a3 3 0 0 1 3-3z" fill="none" stroke="#66857a"/><circle cx="8" cy="6.5" r="1" fill="#66857a"/></symbol>
  <symbol id="icon-phone" viewBox="0 0 16 16"><rect x=".5" y=".5" width="15" height="15" fill="none" stroke="#66857a"/><path d="M5 3.5l2 2-1 1.2c.6 1.4 1.8 2.6 3.2 3.2l1.2-1 2 2-1.3 1.6C7.4 12 4 8.6 3.5 4.8z" fill="none" stroke="#66857a"/></symbol>
  <symbol id="icon-mail" viewBox="0 0 16 16"><rect x=".5" y=".5" width="15" height="15" fill="none" stroke="#66857a"/><rect x="3.5" y="5" width="9" height="6" fill="#66857a"/><path d="M3.5 5l4.5 3.5L12.5 5" fill="none" stroke="#ececec"/></symbol>
  <symbol id="icon-cursor" viewBox="0 0 16 16"><rect x=".5" y=".5" width="15" height="15" fill="none" stroke="#66857a"/><path d="M5 4l6 3-2.4.8L11 11l-1 1-2.4-3.2L6.6 11z" fill="#66857a"/></symbol>
</svg>

<main class="canvas">

  <section class="sheet letterhead" aria-label="Letterhead">
    <svg class="art" width="1128" height="1595" viewBox="0 0 1128 1595">
      <circle class="logo-mark" cx="126" cy="132" r="37" fill="var(--sage)"/>
      <g class="faint-frames" fill="none" stroke="var(--hairline)" stroke-width="2">
        <path d="M1075 1415l60 60-120 120-60-60z"/>
      </g>
      <polygon class="corner-chevron" points="1128,1189 920,1384 912,1392 920,1400 1115,1595 1128,1595 1128,1501 1019,1392 1128,1283" fill="var(--sage)"/>
      <path class="corner-triangle" d="M800 1595L916 1488Q928 1476 940 1488L1055 1595z" fill="var(--charcoal)"/>
      <polygon class="footer-band" points="0,1506 779,1506 731,1553 0,1553" fill="var(--sage)"/>
      <polygon class="footer-stripe-dark" points="787,1506 827,1506 779,1553 739,1553" fill="var(--charcoal)" opacity=".85"/>
      <polygon class="footer-stripe-sage" points="833,1506 845,1506 797,1553 785,1553" fill="var(--sage)"/>
      <circle class="dealer-mark" cx="598" cy="1476" r="19" fill="var(--badge-grey)"/>
    </svg>

    <header class="letter-header">
      <div class="brand-name">CedarlineKTV</div>
      <div class="header-rule"></div>
    </header>

    <div class="abs recipient">
      <b>Rin <span>Halvorsen</span></b><br>
      Designer<br>
      <span class="tag">A</span> : New York City- Zip Code - 000<br>
      <span class="tag">P</span> : +00 123 456 789<br>
      <span class="tag">E</span> : name@email.com
    </div>
    <div class="abs date">December, 2021</div>

    <div class="letter-body">
      <p>Dear Sir,</p>
      <p>Lorem ipsum dolor sit amet, consectetur adipiscing elit, sed do eiusmod tempor incididunt ut labore et dolore magna aliqua. Ut enim ad minim veniam, quis nostrud exercitation ullamco laboris nisi ut aliquip ex ea commodo consequat.</p>
      <p>Duis aute irure dolor in reprehenderit in voluptate velit esse cillum dolore eu fugiat nulla pariatur. Excepteur sint occaecat cupidatat non proident, sunt in culpa qui officia deserunt mollit anim id est laborum. Sed ut perspiciatis unde omnis iste natus error sit voluptatem, nemo enim ipsam quia beatae vitae aut quia.</p>
      <p>Voluptatem accusantium doloremque laudantium, totam rem aperiam, eaque ipsa quae ab illo inventore veritatis et quasi architecto beatae vitae dicta sunt explicabo. Nemo enim ipsam voluptatem quia voluptas sit aspernatur aut odit aut quia consequuntur voluptatem sequi nesciunt.</p>
      <p>Neque porro quisquam dolorem ipsum quia dolor sit amet, consecteturtempora incidunt labore dolore magnam aliquam quaerat voluptatem.</p>
    </div>

    <div class="abs signature"><b>Teo Marchetti</b><br>Manager</div>

    <ul class="contacts">
      <li><svg><use href="#icon-pin"/></svg>418 NW Alder Row, Suite 140 Portland, OR 97209</li>
      <li><svg><use href="#icon-phone"/></svg>555.204.7731</li>
      <li><svg><use href="#icon-mail"/></svg>info@cedarlinektv.com</li>
      <li><svg><use href="#icon-cursor"/></svg>www.cedarlinektv.com</li>
    </ul>

    <div class="abs dealer">Talbot Greaves Certified Dealer</div>
  </section>

  <section class="sheet envelope" aria-label="Envelope">
    <svg class="art" width="1183" height="590" viewBox="0 0 1183 590">
      <circle class="logo-mark" cx="93" cy="109" r="36" fill="var(--sage)"/>
      <g class="faint-frames" fill="none" stroke="var(--hairline)" stroke-width="2">
        <path d="M1125 420l60 60-120 120-60-60z"/>
      </g>
      <polygon class="corner-chevron" points="1183,208 989,389 981,397 989,405 1174,590 1183,590 1183,498 1082,397 1183,296" fill="var(--sage)"/>
      <path class="corner-triangle" d="M869 590L983 486Q995 475 1007 486L1121 590z" fill="var(--charcoal)"/>
      <polygon class="footer-band" points="0,501 854,501 809,546 0,546" fill="var(--sage)"/>
      <polygon class="footer-stripe-dark" points="859,501 899,501 854,546 814,546" fill="var(--charcoal)" opacity=".85"/>
      <polygon class="footer-stripe-sage" points="906,501 917,501 873,546 862,546" fill="var(--sage)"/>
      <circle class="dealer-mark" cx="561" cy="523" r="17" fill="#fff"/>
    </svg>

    <div class="abs brand-name">CedarlineKTV</div>

    <ul class="contacts">
      <li><svg><use href="#icon-pin"/></svg>418 NW Alder Row, Suite 140 Portland, OR 97209</li>
      <li><svg><use href="#icon-phone"/></svg>555.204.7731</li>
    </ul>

    <div class="abs dealer">Talbot Greaves Certified Dealer</div>
  </section>

</main>
</body>
</html>
```